Business card design and logo needed - Photographer

I take photos of weddings, rodeos, snowmobiling.
Need a card to hand out to prospective clients.
Industry/Entity Type
Business
Contact Information for Business Card
Marlon Pettibrook Photography
Requirements
Must have
- Bold
Black or white base.
My website. www.MarlonPettibrook.com
Should not have
- camera/ lens/ aperture blades

```html
<!DOCTYPE html>
<html lang="en">
<head>
<meta charset="utf-8">
<title>Marlon Pettibrook Photography — Business Card</title>
<link rel="stylesheet" href="https://fonts.googleapis.com/css2?family=Bebas+Neue&display=swap">
<style>
  :root {
    --card-base: #303030;
    --brand-lime: #d4ff00;
  }
  html, body {
    margin: 0;
    padding: 0;
    width: 1200px;
    height: 693px;
    overflow: hidden;
    background: var(--card-base);
  }
  .business-card {
    display: block;
    width: 1200px;
    height: 693px;
    background: var(--card-base);
  }
  .card-line {
    font-family: "Bebas Neue", "Oswald", sans-serif;
    fill: var(--brand-lime);
  }
  .card-name { font-size: 283px; }
  .card-trade { font-size: 266px; }
  .card-website { font-size: 170px; }
</style>
</head>
<body>
  <svg class="business-card" viewBox="0 0 1200 693" width="1200" height="693" role="img" aria-label="Marlon Pettibrook Photography, www.MarlonPettibrook.com">
    <text class="card-line card-name" x="51" y="260" textLength="1100" lengthAdjust="spacingAndGlyphs">MARLONPETTIBROOK</text>
    <text class="card-line card-trade" x="51" y="502" textLength="1100" lengthAdjust="spacingAndGlyphs">PHOTOGRAPHY</text>
    <text class="card-line card-website" x="58" y="644" textLength="1086" lengthAdjust="spacingAndGlyphs">WWW.MARLONPETTIBROOK.COM</text>
  </svg>
</body>
</html>
```